Image Ads needed for a Pharmacy Education e-commerce website

I need image ads with these specifications:

Supported formats: JPG, PNG, GIF
File size: 3MB max
Recommended aspect ratios: 1:1 square; 4:5 portrait; 4:3 landscape; 16:9 landscape
Recommended resolutions: 1080x1080 square, 1080x1350 portrait, 1440x1080 landscape, 1920x1080 landscape
Thumbnail: Displays at 400x300 pixels
Thumbnail file size: 500KB max

```html
<!DOCTYPE html>
<html lang="en">
<head>
<meta charset="utf-8">
<title>Dosewell – Unlimited CPE Ceus Ad Set</title>
<link href="https://fonts.googleapis.com/css2?family=Poppins:wght@500;600;700&display=swap" rel="stylesheet">
<style>
  :root {
    --board: #e1903d;
    --panel: #ffffff;
    --navy: #1f3b63;
    --blue: #2b7fcb;
    --blue-deep: #1b6fc4;
    --blue-light: #5db5ee;
    --leaf: #62a43a;
    --band-1: #033e6b;
    --band-2: #1570a6;
    --band-3: #6aa51e;
    --band-4: #e5933f;
    --art-1: #e4e4e7;
    --art-2: #cfd3e8;
  }
  * { margin: 0; padding: 0; box-sizing: border-box; }
  html, body { width: 1200px; height: 1200px; overflow: hidden; }
  body { background: var(--board); font-family: "Poppins", sans-serif; position: relative; }

  .ad {
    position: absolute;
    background: var(--panel);
    overflow: hidden;
    box-shadow: 0 4px 10px rgba(0,0,0,.28);
  }
  .ad--square { left: 92px; top: 143px; width: 425px; height: 425px; }
  .ad--landscape-43 { left: 538px; top: 140px; width: 571px; height: 427px; }
  .ad--portrait { left: 41px; top: 600px; width: 342px; height: 427px; }
  .ad--landscape-169 { left: 405px; top: 601px; width: 757px; height: 425px; }

  .ad__art {
    position: absolute;
    background: linear-gradient(160deg, var(--art-1) 0%, var(--art-2) 100%);
  }
  .ad--square .ad__art { left: 190px; top: 88px; width: 235px; height: 328px; border-radius: 140px 0 0 0; }
  .ad--landscape-43 .ad__art { left: 300px; top: 52px; width: 271px; height: 364px; border-radius: 150px 0 0 0; }
  .ad--portrait .ad__art { left: 0; top: 228px; width: 342px; height: 190px; border-radius: 60px 60px 0 0; }
  .ad--landscape-169 .ad__art { left: 336px; top: 62px; width: 421px; height: 352px; border-radius: 200px 0 0 0; }

  .ad__copy {
    position: absolute;
    display: flex;
    flex-direction: column;
    align-items: center;
    text-align: center;
  }

  .brand {
    display: flex;
    align-items: center;
    gap: 6px;
    color: var(--navy);
    font-weight: 700;
    letter-spacing: -0.5px;
    line-height: 1;
  }
  .brand__dot { border-radius: 50%; background: var(--leaf); }

  .rule { border-top: 2px dotted var(--blue); }

  .headline { color: var(--blue); font-weight: 500; line-height: 1; }
  .subline { color: var(--blue); font-weight: 500; line-height: 1; }
  .price {
    font-weight: 700;
    line-height: 1;
    letter-spacing: 2px;
    background: linear-gradient(135deg, var(--blue-deep) 10%, var(--blue-light) 95%);
    -webkit-background-clip: text;
    background-clip: text;
    color: transparent;
  }

  .band { position: absolute; left: 0; right: 0; bottom: 0; display: flex; }
  .band span:nth-child(1) { flex: 26; background: var(--band-1); }
  .band span:nth-child(2) { flex: 26; background: var(--band-2); }
  .band span:nth-child(3) { flex: 29; background: var(--band-3); }
  .band span:nth-child(4) { flex: 19; background: var(--band-4); }

  /* square 1:1 */
  .ad--square .ad__copy { left: 40px; top: 40px; width: 200px; }
  .ad--square .brand { font-size: 28px; }
  .ad--square .brand__dot { width: 12px; height: 12px; }
  .ad--square .rule { width: 172px; margin-top: 16px; }
  .ad--square .headline { font-size: 36px; margin-top: 6px; }
  .ad--square .subline { font-size: 21px; margin-top: 2px; }
  .ad--square .price { font-size: 96px; margin-top: 4px; }
  .ad--square .rule--end { margin-top: 4px; }
  .ad--square .band { height: 9px; }

  /* landscape 4:3 */
  .ad--landscape-43 .ad__copy { left: 70px; top: 60px; width: 250px; }
  .ad--landscape-43 .brand { font-size: 36px; }
  .ad--landscape-43 .brand__dot { width: 14px; height: 14px; }
  .ad--landscape-43 .rule { width: 210px; margin-top: 22px; }
  .ad--landscape-43 .headline { font-size: 42px; margin-top: 12px; }
  .ad--landscape-43 .subline { font-size: 26px; margin-top: 2px; }
  .ad--landscape-43 .price { font-size: 124px; margin-top: 12px; }
  .ad--landscape-43 .rule--end { margin-top: 10px; }
  .ad--landscape-43 .band { height: 12px; }

  /* portrait 4:5 */
  .ad--portrait .ad__copy { left: 71px; top: 30px; width: 200px; }
  .ad--portrait .brand { font-size: 25px; }
  .ad--portrait .brand__dot { width: 10px; height: 10px; }
  .ad--portrait .rule { width: 139px; margin-top: 14px; }
  .ad--portrait .headline { font-size: 28px; margin-top: 4px; }
  .ad--portrait .subline { font-size: 17px; margin-top: 1px; }
  .ad--portrait .price { font-size: 76px; margin-top: 2px; }
  .ad--portrait .rule--end { margin-top: 2px; }
  .ad--portrait .band { height: 8px; }

  /* landscape 16:9 */
  .ad--landscape-169 .ad__copy { left: 63px; top: 60px; width: 250px; }
  .ad--landscape-169 .brand { font-size: 38px; }
  .ad--landscape-169 .brand__dot { width: 14px; height: 14px; }
  .ad--landscape-169 .rule { width: 210px; margin-top: 20px; }
  .ad--landscape-169 .headline { font-size: 42px; margin-top: 12px; }
  .ad--landscape-169 .subline { font-size: 26px; margin-top: 2px; }
  .ad--landscape-169 .price { font-size: 120px; margin-top: 14px; }
  .ad--landscape-169 .rule--end { margin-top: 8px; }
  .ad--landscape-169 .band { height: 12px; }
</style>
</head>
<body>

  <section class="ad ad--square">
    <div class="ad__art" role="img" aria-label="Illustration of three pharmacists in white lab coats, one holding a medicine bottle and one waving"></div>
    <div class="ad__copy">
      <div class="brand"><span class="brand__dot"></span>Dosewell</div>
      <div class="rule"></div>
      <div class="headline">Unlimited</div>
      <div class="subline">CPE Ceus</div>
      <div class="price">$39</div>
      <div class="rule rule--end"></div>
    </div>
    <div class="band"><span></span><span></span><span></span><span></span></div>
  </section>

  <section class="ad ad--landscape-43">
    <div class="ad__art" role="img" aria-label="Illustration of three pharmacists in white lab coats, one holding a medicine bottle and one waving"></div>
    <div class="ad__copy">
      <div class="brand"><span class="brand__dot"></span>Dosewell</div>
      <div class="rule"></div>
      <div class="headline">Unlimited</div>
      <div class="subline">CPE Ceus</div>
      <div class="price">$39</div>
      <div class="rule rule--end"></div>
    </div>
    <div class="band"><span></span><span></span><span></span><span></span></div>
  </section>

  <section class="ad ad--portrait">
    <div class="ad__art" role="img" aria-label="Illustration of two pairs of pharmacists in lab coats standing on either side, one holding a clipboard"></div>
    <div class="ad__copy">
      <div class="brand"><span class="brand__dot"></span>Dosewell</div>
      <div class="rule"></div>
      <div class="headline">Unlimited</div>
      <div class="subline">CPE Ceus</div>
      <div class="price">$39</div>
      <div class="rule rule--end"></div>
    </div>
    <div class="band"><span></span><span></span><span></span><span></span></div>
  </section>

  <section class="ad ad--landscape-169">
    <div class="ad__art" role="img" aria-label="Illustration of four pharmacists in white lab coats, one holding a clipboard and one waving"></div>
    <div class="ad__copy">
      <div class="brand"><span class="brand__dot"></span>Dosewell</div>
      <div class="rule"></div>
      <div class="headline">Unlimited</div>
      <div class="subline">CPE Ceus</div>
      <div class="price">$39</div>
      <div class="rule rule--end"></div>
    </div>
    <div class="band"><span></span><span></span><span></span><span></span></div>
  </section>

</body>
</html>
```